Business Card For Construction Company
Falcon Erectors
Business Card For Construction Company - Construction
Creative Brief
Professional
Pavel Lunov
No Address
PavelLunov@FalconErectorsCorp.example
www.FalconErectorsCorp.example

```html
<!DOCTYPE html>
<html lang="en">
<head>
<meta charset="utf-8">
<title>Falcon Erectors Stationery</title>
<link rel="stylesheet" href="https://fonts.googleapis.com/css2?family=Michroma&family=Open+Sans:wght@400;600&display=swap">
<style>
  :root {
    --bg: #eceeef;
    --paper: #ffffff;
    --blue: #1f5fb8;
    --blue-deep: #0d3f8a;
    --grey: #5f6368;
    --text: #3b3f45;
    --faint: #eef1f5;
  }
  * { box-sizing: border-box; margin: 0; padding: 0; }
  html, body { width: 1200px; height: 936px; overflow: hidden; }
  body { background: var(--bg); font-family: "Open Sans", sans-serif; color: var(--text); position: relative; }

  .sheet { position: absolute; background: var(--paper); overflow: hidden; }
  .band { position: absolute; left: 0; width: 100%; display: block; }

  .brand { display: flex; align-items: center; gap: 6px; }
  .brand-mark { background: var(--blue); flex: none; }
  .brand-name { font-family: "Michroma", sans-serif; color: var(--blue); text-transform: uppercase; line-height: 1.1; white-space: nowrap; }

  .contact { font-size: 6px; line-height: 1.6; color: var(--text); }
  .contact span { display: block; white-space: nowrap; }

  .faint-square { position: absolute; background: var(--faint); }

  /* Letterhead */
  .letterhead { left: 197px; top: 56px; width: 375px; height: 556px; }
  .letterhead .brand { position: absolute; left: 24px; top: 36px; }
  .letterhead .brand-mark { width: 12px; height: 12px; }
  .letterhead .brand-name { font-size: 9px; }
  .letterhead .contact { position: absolute; left: 230px; top: 33px; }
  .letterhead .faint-square { left: 60px; top: 240px; width: 110px; height: 110px; }
  .letterhead .band { bottom: 12px; height: 10px; }

  /* Folder */
  .folder { left: 633px; top: 56px; width: 374px; height: 556px; }
  .folder .brand { position: absolute; left: 0; right: 0; top: 250px; justify-content: center; gap: 10px; }
  .folder .brand-mark { width: 24px; height: 24px; }
  .folder .brand-name { font-size: 16px; }
  .folder .band { bottom: 12px; height: 10px; }

  /* Business card front */
  .card-front { left: 84px; top: 658px; width: 151px; height: 89px; }
  .card-front .brand { position: absolute; left: 12px; top: 12px; gap: 4px; }
  .card-front .brand-mark { width: 9px; height: 9px; }
  .card-front .brand-name { font-size: 6.5px; }
  .card-front .person { position: absolute; left: 12px; top: 34px; font-size: 5px; line-height: 1.5; }
  .card-front .person strong { font-weight: 600; color: var(--blue-deep); font-size: 5.5px; }
  .card-front .contact { position: absolute; left: 12px; top: 56px; font-size: 4.5px; }

  /* Business card back */
  .card-back { left: 84px; top: 764px; width: 151px; height: 91px; }
  .card-back .faint-square { left: 16px; top: 16px; width: 58px; height: 58px; }
  .card-back .web { position: absolute; left: 12px; bottom: 8px; font-size: 4.5px; color: var(--grey); }

  /* Envelope front */
  .envelope-front { left: 266px; top: 666px; width: 321px; height: 207px; }
  .envelope-front .brand { position: absolute; left: 14px; top: 20px; }
  .envelope-front .brand-mark { width: 10px; height: 10px; }
  .envelope-front .brand-name { font-size: 8px; }
  .envelope-front .band { bottom: 14px; height: 10px; }

  /* Envelope back */
  .envelope-back { left: 633px; top: 666px; width: 377px; height: 207px; }
  .envelope-back .flap { position: absolute; left: 0; top: 0; width: 100%; height: 90px; display: block; }
  .envelope-back .web { position: absolute; left: 0; right: 0; top: 28px; text-align: center; font-size: 7px; letter-spacing: 3px; color: #ffffff; }
</style>
</head>
<body>

<section class="sheet letterhead">
  <div class="brand"><span class="brand-mark"></span><span class="brand-name">Falcon Erectors</span></div>
  <div class="contact">
    <span>T: 555 010 2040</span>
    <span>F: 555 010 2041</span>
    <span>PavelLunov@FalconErectorsCorp.example</span>
    <span>www.FalconErectorsCorp.example</span>
  </div>
  <div class="faint-square"></div>
  <svg class="band" viewBox="0 0 100 10" preserveAspectRatio="none">
    <defs><linearGradient id="blueBandA" x1="0" x2="1"><stop offset="0" stop-color="#0d3f8a"/><stop offset="1" stop-color="#2e78d6"/></linearGradient></defs>
    <polygon points="0,0 59,0 55,10 0,10" fill="url(#blueBandA)"/>
    <polygon points="60,0 100,0 100,10 56,10" fill="#6a6f75"/>
  </svg>
</section>

<section class="sheet folder">
  <div class="brand"><span class="brand-mark"></span><span class="brand-name">Falcon Erectors</span></div>
  <svg class="band" viewBox="0 0 100 10" preserveAspectRatio="none">
    <defs><linearGradient id="blueBandB" x1="0" x2="1"><stop offset="0" stop-color="#0d3f8a"/><stop offset="1" stop-color="#2e78d6"/></linearGradient></defs>
    <polygon points="0,0 59,0 55,10 0,10" fill="url(#blueBandB)"/>
    <polygon points="60,0 100,0 100,10 56,10" fill="#6a6f75"/>
  </svg>
</section>

<section class="sheet card-front">
  <div class="brand"><span class="brand-mark"></span><span class="brand-name">Falcon Erectors</span></div>
  <div class="person"><strong>Pavel Lunov</strong><br>Project Manager</div>
  <div class="contact">
    <span>T: 555 010 2040</span>
    <span>PavelLunov@FalconErectorsCorp.example</span>
  </div>
</section>

<section class="sheet card-back">
  <div class="faint-square"></div>
  <div class="web">www.FalconErectorsCorp.example</div>
</section>

<section class="sheet envelope-front">
  <div class="brand"><span class="brand-mark"></span><span class="brand-name">Falcon Erectors</span></div>
  <svg class="band" viewBox="0 0 100 10" preserveAspectRatio="none">
    <defs><linearGradient id="blueBandC" x1="0" x2="1"><stop offset="0" stop-color="#0d3f8a"/><stop offset="1" stop-color="#2e78d6"/></linearGradient></defs>
    <polygon points="0,0 62,0 59,10 0,10" fill="url(#blueBandC)"/>
    <polygon points="63,0 100,0 100,10 60,10" fill="#6a6f75"/>
  </svg>
</section>

<section class="sheet envelope-back">
  <svg class="flap" viewBox="0 0 377 90" preserveAspectRatio="none">
    <defs><linearGradient id="flapBlue" x1="0" x2="1"><stop offset="0" stop-color="#0d3f8a"/><stop offset="0.5" stop-color="#2e78d6"/><stop offset="1" stop-color="#0d3f8a"/></linearGradient></defs>
    <polygon points="0,0 377,0 377,62 188,86 0,62" fill="url(#flapBlue)"/>
  </svg>
  <div class="web">www.FalconErectorsCorp.example</div>
</section>

</body>
</html>
```